Venmark Power Web Design

I want a design for a home page that can function as a template for the entire web design. I"m also requesting that the design be adapted as a template for Power Point presentations, as well.

Here"s a brief about our company:

Venmark Power provides its customers with clean, redundant and reliable power. Functioning as a private power producer, Venmark Power owns and operates combined heat and power (CHP) and distributed generation (DG) systems.

Venmark’s management has extensive experience in aerospace turbines engine operation, maintenance, manufacturing and repair. Depending on the customer need, Venmark either builds new generators or refurbish “retired” aerospace turbines into industrial generators. This allows Venmark to deliver generating systems at greatly reduced capital outlays, enabling Venmark Power to offer its customers not only redundant power and grid independence, but significant savings on their energy needs. Venmark’s typical installation size is 500Kws to 3Mws but based upon our customer"s needs, Venmark can site multiple generators to configure systems of larger size.

By using aero derivative turbine engines the company has the flexibility to use the best source of fuel for each site and power requirement. The turbine engine can operate on virtually any combustible fuel. This allows Venmark to utilize the flex fuel practice and operate on either the least expensive fuel available or operate on renewable and biofuels to fulfill the green power requirements mandated by many federal, state and local utility commissions.

Venmark’s market strategy is as follows:

1. Sell reliable and redundant power through a PPAs or lease agreements to industrial or institutional customers with high electrical and thermal needs such as food processors, bio fuel producers, hospitals, casinos, hotels, etc.

2. Lease its systems to customer that “flare gas” as byproducts of their processes such as wastewater treatment facilities, land fills and "stranded gas wells" allowing them to use their waste products to power their facilities and sell excess electricity back to the grid.

3. Partner with other private power producers to provide the turbine generating capacity on a leased basis.
Updates

Please disregard the "turbine logo" that was uploaded as a file and focus only on the "bolt design logo", A (bolt) E.

We like the simple navigation and clean and modern design of sites.

http://www.plusoria.example/

http://www.gravunet.example/

http://www.tovelspace.example/

Target Market(s)

Our target markets can be found on the web architecture file I've attached to this submission.

Number of Pages Required

1 page

Requirements
Must have
• The designer must provide a web design and a Power Point template based upon the web design.

• The design must contemplate the web architecture that I""ve included as a file.

```html
<!DOCTYPE html>
<html lang="en">
<head>
<meta charset="utf-8">
<title>Venmark Power – Home</title>
<link href="https://fonts.googleapis.com/css2?family=Ubuntu:wght@300;400;500&family=PT+Sans:wght@400;700&display=swap" rel="stylesheet">
<style>
:root{
  --page:#fef7e9;
  --green:#8cbd3c;
  --green-dark:#6f9a2a;
  --frame:#a4cc66;
  --tile-outer:#8ea944;
  --tile-top:#a2c655;
  --tile-bottom:#6e8f2c;
  --tile-text:#f4e98c;
  --gold:#c9a53a;
  --brand:#2f9a3c;
  --ink:#1c1c1c;
  --footer-link:#6d7d1f;
  --red:#e0261f;
}
*{box-sizing:border-box;margin:0;padding:0}
html,body{width:1092px;height:1200px;overflow:hidden;background:var(--page)}
body{position:relative;font-family:"PT Sans",sans-serif;color:var(--ink)}
a{text-decoration:none}
.main-nav{position:absolute;left:31px;top:35px;width:1027px;height:51px;border:1px solid var(--green-dark);
  background:linear-gradient(#b3dc65,var(--green) 55%,#7fb032);display:flex;align-items:stretch;justify-content:space-between;padding:2px 30px 2px 2px}
.main-nav a{font-family:"Ubuntu",sans-serif;font-size:19px;color:#fff;white-space:nowrap;display:flex;align-items:center;padding:0 10px}
.main-nav a.active{background:linear-gradient(#6fa82a,#5a9421);color:#111;padding:0 26px 0 28px;margin-right:14px}
.hero{position:absolute;left:30px;top:117px;width:1031px;height:447px;background:var(--frame);padding:14px}
.hero-inner{position:relative;width:100%;height:100%;background:#fff;overflow:hidden}
.hero-art{position:absolute;left:0;top:0;width:640px;height:100%;
  background:linear-gradient(90deg,#9cbf3a 0%,#b5d05a 35%,#cfe4ef 65%,rgba(255,255,255,0) 100%)}
.brand{position:absolute;left:500px;top:28px;display:flex;align-items:center;gap:16px}
.brand-dot{width:86px;height:86px;border-radius:50%;background:var(--green)}
.brand-name{font-family:"Ubuntu",sans-serif;font-size:50px;font-weight:400;color:var(--brand);line-height:1;white-space:nowrap}
.hero-copy{position:absolute;left:381px;top:170px;width:610px}
.hero-copy h1{font-family:"Ubuntu",sans-serif;font-weight:300;font-size:30px;color:#222;margin-bottom:18px;letter-spacing:-.5px;white-space:nowrap}
.hero-copy h1 span{color:var(--gold)}
.hero-copy p{font-size:13.5px;line-height:20px;margin-bottom:20px}
.hero-copy b{color:var(--brand);font-weight:400}
.read-more{font-size:12.5px;font-weight:700;color:#1f4a12}
.tile{position:absolute;top:601px;width:320px;height:153px;background:var(--tile-outer);padding:9px;box-shadow:0 8px 6px -4px rgba(0,0,0,.25)}
.tile span{display:flex;width:100%;height:100%;align-items:center;justify-content:center;text-align:center;
  background:linear-gradient(var(--tile-top),var(--tile-bottom));font-family:"Ubuntu",sans-serif;font-weight:300;font-size:25px;line-height:27px;color:var(--tile-text)}
.section-title{position:absolute;left:30px;top:788px;font-family:"Ubuntu",sans-serif;font-weight:300;font-size:28px;color:var(--gold)}
.rule{position:absolute;left:30px;width:1032px;border-top:1px dashed #555}
.strategy{position:absolute;left:30px;top:875px;width:700px;font-size:13.5px;line-height:20px}
.strategy li{list-style:none;margin-bottom:20px}
.strategy b{font-size:14px}
.support{position:absolute;left:762px;top:879px;width:300px;height:176px;border:1px solid var(--green-dark);background:#fff;padding:10px 14px;overflow:hidden}
.support .big{font-family:"Ubuntu",sans-serif;font-size:34px;color:var(--red);font-weight:500;letter-spacing:-1px}
.support .online{font-family:"Ubuntu",sans-serif;font-size:22px;color:#222}
.support .word{font-family:"Ubuntu",sans-serif;font-size:36px;color:#111;line-height:36px;letter-spacing:1px}
.support .line{font-family:"Ubuntu",sans-serif;font-size:18px;color:#333;margin-top:6px;white-space:nowrap}
.support .mail{font-family:"Ubuntu",sans-serif;font-size:17px;color:#6a8a2a;line-height:22px;white-space:nowrap}
.support svg{position:absolute;right:8px;top:8px}
.footer-nav{position:absolute;left:0;top:1125px;width:1092px;display:flex;justify-content:center;gap:40px}
.footer-nav a{font-size:13px;font-weight:700;color:var(--footer-link);white-space:nowrap}
.copyright{position:absolute;left:0;top:1152px;width:1092px;text-align:center;font-size:12.5px;font-weight:700;color:var(--footer-link)}
</style>
</head>
<body>
<nav class="main-nav">
  <a class="active" href="#">Home</a>
  <a href="#">About Venmark</a>
  <a href="#">CHP</a>
  <a href="#">Stranded Gas</a>
  <a href="#">Resources</a>
  <a href="#">Partners &amp; Suppliers</a>
  <a href="#">Contact Us</a>
</nav>

<section class="hero">
  <div class="hero-inner">
    <div class="hero-art" role="img" aria-label="Green wind turbines against a pale blue sky"></div>
    <div class="brand"><div class="brand-dot"></div><div class="brand-name">Venmark Power</div></div>
    <div class="hero-copy">
      <h1>welcome to <span>VENMARK POWER</span></h1>
      <p><b>Venmark Power</b> provides its customers with clean, redundant and reliable power. Functioning as a private power producer, Venmark Power owns and operates combined heat and power (CHP) and distributed generation (DG) systems.</p>
      <p>Venmark’s management has extensive experience in aerospace turbines engine operation, maintenance, manufacturing and repair. Depending on the customer need, Venmark either builds new generators or refurbish “retired” aerospace turbines into industrial generators.</p>
      <a class="read-more" href="#">Read More...</a>
    </div>
  </div>
</section>

<a class="tile" style="left:30px" href="#"><span>Texas CHP Critical<br>Infrastructure Legislation</span></a>
<a class="tile" style="left:387px" href="#"><span>Is your Business a Good<br>Candidate For CHP</span></a>
<a class="tile" style="left:742px" href="#"><span>CHP Calculator</span></a>

<h2 class="section-title">Our Marketing Strategy</h2>
<div class="rule" style="top:832px"></div>

<ol class="strategy">
  <li><b>1.</b> Sell reliable and redundant power through a PPAs or lease agreements to industrial or institutional customers with high electrical and thermal needs such as food processors, bio fuel producers, hospitals, casinos, hotels, etc.</li>
  <li><b>2.</b> Lease its systems to customer that “flare gas” as byproducts of their processes such as wastewater treatment facilities, land fills and "stranded gas wells" allowing them to use their waste products to power their facilities and sell excess electricity back to the grid.</li>
  <li><b>3.</b> Partner with other private power producers to provide the turbine generating capacity on a leased basis.</li>
</ol>

<aside class="support">
  <svg width="90" height="54" viewBox="0 0 96 56" aria-hidden="true">
    <path d="M10 18 Q48 -4 86 18 L80 28 Q70 22 64 24 L62 18 Q48 12 34 18 L32 24 Q26 22 16 28 Z" fill="var(--red)"/>
    <path d="M28 28 L68 28 L78 52 L18 52 Z" fill="var(--red)"/>
    <circle cx="48" cy="38" r="9" fill="#fff"/><circle cx="48" cy="38" r="4" fill="var(--red)"/>
  </svg>
  <div><span class="big">24 x 7</span> <span class="online">ONLINE</span></div>
  <div class="word">SUPPORT</div>
  <div class="line">00 18 55420 55420</div>
  <div class="line" style="margin-top:8px">mail Us at:</div>
  <div class="mail">support@venmarkpower.example</div>
</aside>

<div class="rule" style="top:1100px"></div>
<nav class="footer-nav">
  <a href="#">Home</a><a href="#">About Venmark</a><a href="#">CHP</a><a href="#">Stranded Gas</a><a href="#">Resources</a><a href="#">Partners &amp; Suppliers</a><a href="#">Contact Us</a>
</nav>
<p class="copyright">© 2010-'11 VENMARK POWER &nbsp;&nbsp;|&nbsp;&nbsp; ALL RIGHTS RESERVED</p>
</body>
</html>
```